Double-Sided Table Top Flyer to Match Attached Marketing Materials

Please read this carefully. Must follow instructions. Do not submit multiple designs that look similar. Submit the front and back together as one submission. Do not submit the front and back separately. I have attached my new rack card design, business card design and gift card design. Colors, shapes and style match. I want a table top flyer to match them using same colors, shapes and style. The flyer will be 282.4 mm tall by 218.9 mm wide. See attached FLYER SPECs which shows full bleed, trim and safety area dimensions. THE FRONT: The main focus of the front is an "Harbor Sunset Drawing". This should be the main focus / font centered on the front. Under this there should be the attached paragraph. The front will also use the attached "PROFILE PIRATE" picture. The front will also incorporate my primary logo for "Skipper Dalloway's Sail Lessons & Cruises, LLC" as well as the badges of "Licensed Captain", "Instructor" and "Licensed Captain". Please incorporate the attached family beach day photo somehow. It may be set in the background as transparent. Designer's choice of how to incorporate. FOR THE BACK: Take most of the content from the front of the attached rack card. If additional content is required for the back please include as much as you can from the back of the attached rack card. The front has the three small pictures. The back has the one picture of me and the three logos towards the bottom. The content on the front of rack card takes priority over the content on back.

Target Market(s)

see attachments.

Industry/Entity Type

see attachments.

Font styles to use
Other font styles liked:
• The font type I use most is Good Timing RG from glyphbarnery.com

Requirements
Must have
• see attachments.
Nice to have
• see attachments.
Should not have
• see attachments.

```html
<!DOCTYPE html>
<html lang="en">
<head>
<meta charset="utf-8">
<title>Harbor Sunset Drawing – Table Top Flyer</title>
<link href="https://fonts.googleapis.com/css2?family=Montserrat:wght@400;500;600;700;800;900&display=swap" rel="stylesheet">
<style>
:root{
  --backdrop:#8c8c8c;
  --paper:#f4f4f4;
  --ink:#2a2a2a;
  --dark:#262626;
  --red:#e21c3d;
  --gold:#d2ab2b;
  --white:#ffffff;
  --sky:#bcd6ea;
}
*{box-sizing:border-box;margin:0;padding:0}
html,body{width:1200px;height:762px;overflow:hidden;background:var(--backdrop);font-family:"Montserrat",sans-serif;color:var(--ink)}
.flyer{position:absolute;width:505px;height:652px;background:var(--paper);overflow:hidden}
.flyer--front{left:70px;top:50px}
.flyer--back{left:629px;top:49px}
.flyer svg.shapes{position:absolute;left:0;top:0;width:100%;height:100%}
.abs{position:absolute}

/* front */
.brand-mark{left:46px;top:37px;width:146px;height:146px;border-radius:50%;background:var(--red);display:flex;align-items:center;justify-content:center}
.brand-mark__inner{width:124px;height:124px;border-radius:50%;background:var(--dark);display:flex;align-items:center;justify-content:center;text-align:center;padding:14px;color:var(--white);font-weight:700;font-size:10.5px;line-height:1.25}
.title{left:31px;top:250px;font-weight:900;font-size:47px;letter-spacing:-1px;color:var(--ink);line-height:1}
.subtitle{left:32px;top:298px;font-weight:900;font-size:28px;line-height:1;letter-spacing:.3px}
.subtitle .gold{color:var(--gold)}
.subtitle .red{color:var(--red)}
.intro{left:32px;top:331px;width:452px;font-size:12.2px;line-height:14.6px;color:var(--ink)}
.services{left:29px;top:437px;width:320px}
.service{position:absolute;display:flex;align-items:center;gap:9px;font-size:10.6px;line-height:12.8px;font-weight:500;white-space:nowrap}
.service--col1{width:146px}
.service--col2{width:158px}
.service::after{content:"";position:absolute;left:39px;right:0;bottom:-8px;height:1px;background:var(--gold)}
.service--last::after{display:none}
.hex{flex:none;width:30px;height:27px;clip-path:polygon(25% 0,75% 0,100% 50%,75% 100%,25% 100%,0 50%);display:flex;align-items:center;justify-content:center}
.hex--red{background:var(--red)}
.hex--dark{background:var(--dark)}
.hex span{width:10px;height:10px;border:1.6px solid var(--white);border-radius:50%}
.badge{border-radius:50%;background:var(--dark);border:3px solid var(--gold)}
.badge--red{background:var(--red);border-color:var(--dark)}
.badge--light{background:#dfe7ef;border-color:#29507f}
.cta{right:28px;text-align:right;color:var(--white);font-weight:800;font-size:12.4px;line-height:14px;letter-spacing:.3px}
.phone{right:28px;display:flex;align-items:center;gap:4px;color:var(--white);font-weight:700;font-size:25px;line-height:1}
.phone svg{width:22px;height:22px}
.email{right:28px;color:var(--white);font-size:11px;display:flex;gap:4px;align-items:center}
.web{right:28px;color:var(--white);font-weight:800;font-size:14px;letter-spacing:.6px}
.web .gold{color:var(--gold)}

/* back */
.owner{left:31px;top:20px;color:var(--white);font-weight:900;font-size:21px;letter-spacing:.6px}
.owner-role{left:31px;top:44px;color:var(--gold);font-weight:700;font-size:13.5px;letter-spacing:.4px}
.cert-head{left:154px;top:66px;color:var(--gold);font-weight:800;font-size:10.5px;letter-spacing:.2px}
.cert-copy{left:154px;top:81px;width:240px;color:var(--white);font-size:7.8px;line-height:9.8px}
.phone-tag{left:154px;top:139px;width:146px;height:20px;background:var(--red);clip-path:polygon(6% 0,100% 0,94% 100%,0 100%);display:flex;align-items:center;justify-content:center;gap:3px;color:var(--white);font-weight:700;font-size:13.5px}
.phone-tag svg{width:13px;height:13px}
.small-email{left:164px;top:165px;color:var(--white);font-size:8.5px}
.small-web{left:164px;top:177px;color:var(--gold);font-weight:800;font-size:8px}
.about-label{left:181px;top:301px;color:var(--gold);font-weight:900;font-size:26px;letter-spacing:.5px;line-height:1}
.about-rule{left:283px;top:246px;width:1.5px;height:78px;background:var(--gold)}
.about-copy{left:294px;top:246px;width:200px;font-size:11px;line-height:13.7px;color:var(--ink);font-weight:500}
.cred{position:absolute;top:347px;height:85px;background:var(--dark);clip-path:polygon(0 0,88% 0,100% 50%,88% 100%,0 100%);display:flex;align-items:center;color:var(--white);font-weight:700;font-size:14px;line-height:16.5px}
.cred-hex{position:absolute;top:358px;width:66px;height:60px;clip-path:polygon(25% 0,75% 0,100% 50%,75% 100%,25% 100%,0 50%);display:flex;align-items:center;justify-content:center}
.cred-hex span{width:22px;height:22px;border:2.5px solid var(--white);border-radius:5px}
</style>
</head>
<body>

<!-- FRONT -->
<section class="flyer flyer--front">
  <svg class="shapes" viewBox="0 0 505 652" preserveAspectRatio="none" aria-hidden="true">
    <polygon points="0,0 210,0 0,40" fill="var(--sky)"/>
    <polygon points="0,32 0,78 233,243 233,196" fill="var(--red)"/>
    <polygon points="418,199 505,149 505,190 418,238" fill="var(--gold)"/>
    <polygon points="303,532 505,532 505,569 285,569" fill="var(--red)"/>
    <polygon points="285,569 505,569 505,652 131,652" fill="var(--dark)"/>
    <polygon points="258,574 270,581 205,637 193,631" fill="var(--red)"/>
  </svg>
  <div class="abs" role="img" aria-label="Smiling captain in a pirate costume with tricorn hat in front of a skull-and-crossbones flag"
       style="left:170px;top:0;width:335px;height:250px;background:linear-gradient(135deg,#6a7fa3,#2d2f3a 55%,#b8323d);clip-path:polygon(0 0,100% 0,100% 58%,58% 100%,18% 100%,10% 40%)"></div>
  <div class="abs brand-mark"><div class="brand-mark__inner">Skipper Dalloway's Sail Lessons &amp; Cruises, LLC</div></div>

  <h1 class="abs title">HARBOR</h1>
  <h2 class="abs subtitle"><span class="gold">SUNSET</span> <span class="red">DRAWING</span></h2>
  <p class="abs intro">This island excursion is for a boat outing leaving from Bayport going to a barrier island such as Gull Key or Pelican Bar. This package includes the boat, a licensed captain and fuel. The duration will be approximately four to six hours. The winner of raffle may bring up to a total of six passengers. The winner is responsible for their own provisions such as ice, drinks and food.</p>

  <div class="abs services">
    <div class="service service--col1" style="left:0;top:0"><div class="hex hex--red"><span></span></div>Hands-on Boat<br>Training</div>
    <div class="service service--col1" style="left:0;top:44px"><div class="hex hex--dark"><span></span></div>Introduction<br>to Power Boating</div>
    <div class="service service--col1" style="left:0;top:89px"><div class="hex hex--red"><span></span></div>Precision Docking<br>&amp; Boat Handling</div>
    <div class="service service--col1 service--last" style="left:0;top:134px"><div class="hex hex--dark"><span></span></div>Open Water<br>Boating Handling</div>
    <div class="service service--col2" style="left:151px;top:0"><div class="hex hex--red"><span></span></div>Open Water<br>Advanced Maneuvers</div>
    <div class="service service--col2" style="left:151px;top:44px"><div class="hex hex--dark"><span></span></div>Captaining/<br>Piloting Service for<br>Your Outings</div>
    <div class="service service--col2 service--last" style="left:151px;top:89px"><div class="hex hex--red"><span></span></div>Costal<br>Navigation</div>
  </div>

  <div class="abs badge badge--light" style="left:346px;top:474px;width:42px;height:42px"></div>
  <div class="abs badge" style="left:392px;top:473px;width:44px;height:44px"></div>
  <div class="abs badge badge--red" style="left:440px;top:473px;width:44px;height:44px"></div>

  <p class="abs cta" style="top:539px">TO INQUIRE SEND<br>A TEXT TODAY!</p>
  <p class="abs phone" style="top:579px"><svg viewBox="0 0 24 24"><circle cx="12" cy="12" r="10.5" fill="none" stroke="var(--gold)" stroke-width="2"/><path d="M8.5 6.5l2 2.5-1.2 1.4c.7 1.6 1.9 2.8 3.4 3.5l1.3-1.2 2.5 2-1 1.7c-3.8.2-8.2-4.4-8.3-8.2z" fill="var(--gold)"/></svg>(555) 014-2290</p>
  <p class="abs email" style="top:607px">✉ hello@harborhelmsman.com</p>
  <p class="abs web" style="top:622px">www.<span class="gold">harborhelmsman</span>.com</p>
</section>

<!-- BACK -->
<section class="flyer flyer--back">
  <svg class="shapes" viewBox="0 0 505 652" preserveAspectRatio="none" aria-hidden="true">
    <polygon points="0,0 505,0 505,25 135,309 0,205" fill="var(--dark)"/>
    <polygon points="295,195 505,33 505,63 295,229" fill="var(--red)"/>
    <polygon points="0,208 92,268 92,298 0,240" fill="var(--gold)"/>
    <polygon points="305,534 505,534 505,571 287,571" fill="var(--red)"/>
    <polygon points="287,571 505,571 505,652 130,652" fill="var(--dark)"/>
    <polygon points="260,576 272,583 207,639 195,633" fill="var(--red)"/>
  </svg>
  <div class="abs" role="img" aria-label="Portrait of the owner and captain in a light grey polo shirt"
       style="left:6px;top:70px;width:144px;height:222px;background:linear-gradient(180deg,#3a3a3a,#9aa0a6 60%,#7c838a)"></div>

  <h1 class="abs owner">REED T. HALVORSEN</h1>
  <p class="abs owner-role">OWNER &amp; CAPTAIN</p>
  <p class="abs cert-head">CERTIFIED INSTRUCTOR</p>
  <p class="abs cert-copy">Don't overpay elsewhere. All training that is conducted by any qualified person or company is based offof nationally accredited and recognized content and curriculum developed by the National Boating Safety Board or the Coastal Boating Guild.</p>
  <p class="abs phone-tag"><svg viewBox="0 0 24 24"><circle cx="12" cy="12" r="10.5" fill="none" stroke="var(--gold)" stroke-width="2"/><path d="M8.5 6.5l2 2.5-1.2 1.4c.7 1.6 1.9 2.8 3.4 3.5l1.3-1.2 2.5 2-1 1.7c-3.8.2-8.2-4.4-8.3-8.2z" fill="var(--gold)"/></svg>(555) 014-2290</p>
  <p class="abs small-email">✉ hello@harborhelmsman.com</p>
  <p class="abs small-web">www.Harbor-Helmsman.com</p>

  <p class="abs about-label">ABOUT</p>
  <div class="abs about-rule"></div>
  <p class="abs about-copy">CMA Licensed Master Captain &amp; National Boating Safety Board Certified Boating Instructor providing hands-on boat training &amp; captaining services with your boat at your location.</p>

  <div class="cred" style="left:56px;width:121px;padding-left:42px">Retired<br>Military</div>
  <div class="cred" style="left:202px;width:120px;padding-left:43px">Graduate<br>Degree</div>
  <div class="cred" style="left:347px;width:136px;padding-left:41px">Current<br>Security<br>Clearance</div>
  <div class="cred-hex" style="left:26px;background:var(--red)"><span></span></div>
  <div class="cred-hex" style="left:172px;background:var(--gold)"><span></span></div>
  <div class="cred-hex" style="left:316px;background:var(--red)"><span></span></div>

  <div class="abs" role="img" aria-label="Woman in a tank top preparing a boat on a trailer at the water's edge"
       style="left:31px;top:457px;width:112px;height:119px;background:linear-gradient(160deg,#6f8f5c,#b9a98a);clip-path:polygon(8% 0,100% 0,96% 100%,0 100%)"></div>
  <div class="abs" role="img" aria-label="Man in a blue shirt tying a line on a dock"
       style="left:137px;top:457px;width:115px;height:119px;background:linear-gradient(160deg,#3d6f8a,#c9c2b4);clip-path:polygon(8% 0,100% 0,96% 100%,0 100%)"></div>

  <div class="abs badge badge--light" style="left:306px;top:456px;width:50px;height:50px"></div>
  <div class="abs badge" style="left:366px;top:454px;width:54px;height:54px"></div>
  <div class="abs badge badge--red" style="left:429px;top:454px;width:54px;height:54px"></div>

  <p class="abs cta" style="top:541px">TO INQUIRE SEND<br>A TEXT TODAY!</p>
  <p class="abs phone" style="top:582px"><svg viewBox="0 0 24 24"><circle cx="12" cy="12" r="10.5" fill="none" stroke="var(--gold)" stroke-width="2"/><path d="M8.5 6.5l2 2.5-1.2 1.4c.7 1.6 1.9 2.8 3.4 3.5l1.3-1.2 2.5 2-1 1.7c-3.8.2-8.2-4.4-8.3-8.2z" fill="var(--gold)"/></svg>(555) 014-2290</p>
  <p class="abs email" style="top:610px">✉ hello@harborhelmsman.com</p>
  <p class="abs web" style="top:625px">www.<span class="gold">harborhelmsman</span>.com</p>
</section>

</body>
</html>
```